Home Design company focused on remodel and enhancement of kitchens and bathroorms

I already have a logo designed by ArtHarbor, I now need a design for my business cards.
The company is in the remodeling and enhancement industry for homes, focusing on kitchens and bathrooms, however, we can remodel or enhance every room in a home, an office space, etc.

The company's name is VELMOR HOME DESIGN, LLC

We'll focus on clients in the Rio Grande Valley, Texas. Primarily McAllen, Edinburg, Pharr, Mission, Brownsville and South Padre Island.

The design on the business card should transmit reliability, professionalism anda bit of upscale design.

The logo is in black and white, and would like to keep it that way.

The information that needs to be printed in the business cards is:
Company's name: Velmor Home Design
Company's Logo (attached)
My name: Noel Bramwit
Address, phone and email:
2715 N Parkline Road, Ste 348
McAllen, TX 78501
(555) 010 0187
nbramwit@velmordesign.example
Website: velmordesign.example

```html
<!DOCTYPE html>
<html lang="en">
<head>
<meta charset="utf-8">
<title>Velmor Home Design — Business Card</title>
<link href="https://fonts.googleapis.com/css2?family=Open+Sans:wght@400;700&display=swap" rel="stylesheet">
<style>
  :root {
    --backdrop: #8e908f;
    --ink: #000000;
    --paper: #ebebee;
    --paper-text: #e6e6e8;
  }
  * { margin: 0; padding: 0; box-sizing: border-box; }
  html, body {
    width: 1200px; height: 1200px; overflow: hidden;
    background: var(--backdrop);
    font-family: "Open Sans", sans-serif;
  }
  .card {
    position: absolute;
    left: 209px;
    width: 797px;
    height: 440px;
    overflow: hidden;
    background: var(--ink);
  }
  .card--front { top: 99px; }
  .card--back { top: 634px; }

  .front-band {
    position: absolute; left: 0; top: 0;
    width: 100%; height: 208px;
    background: var(--paper);
  }
  .wordmark {
    position: absolute;
    text-transform: uppercase;
    font-weight: 400;
    letter-spacing: 0.34em;
    line-height: 1;
    white-space: nowrap;
  }
  .wordmark span { display: block; }
  .front-band .wordmark {
    left: 61px; top: 37px;
    font-size: 41px;
    color: var(--ink);
  }
  .front-band .wordmark span { height: 43px; }

  .holder {
    position: absolute; left: 63px; top: 236px;
    color: var(--paper-text);
  }
  .holder__name { font-size: 37px; font-weight: 700; line-height: 46px; white-space: nowrap; }
  .holder__role { font-size: 20px; font-weight: 400; line-height: 26px; }

  .contacts {
    position: absolute; left: 63px; top: 324px;
    list-style: none;
    color: var(--paper-text);
    font-size: 20px;
    line-height: 28px;
    white-space: nowrap;
  }
  .contacts li { display: flex; align-items: center; gap: 10px; }
  .contacts svg { width: 18px; height: 18px; flex: none; }

  .address {
    position: absolute; right: 60px; top: 352px;
    text-align: right;
    color: var(--paper-text);
    font-size: 20px;
    line-height: 28px;
    font-style: normal;
    white-space: nowrap;
  }

  .back-mark {
    position: absolute; left: 150px; top: 169px;
    width: 104px; height: 104px;
    border: 10px solid var(--paper-text);
  }
  .back-divider {
    position: absolute; left: 436px; top: 169px;
    width: 3px; height: 104px;
    background: var(--paper-text);
  }
  .card--back .wordmark {
    left: 462px; top: 164px;
    font-size: 35px;
    color: var(--paper-text);
  }
  .card--back .wordmark span { height: 39px; }
</style>
</head>
<body>

<section class="card card--front" aria-label="Business card front">
  <div class="front-band">
    <h1 class="wordmark"><span>Velmor</span><span>Home</span><span>Design</span></h1>
  </div>

  <div class="holder">
    <p class="holder__name">Noel Bramwit</p>
    <p class="holder__role">Founder &amp; CEO</p>
  </div>

  <ul class="contacts">
    <li>
      <svg viewBox="0 0 24 24" fill="none" stroke="#e6e6e8" stroke-width="2" stroke-linecap="round" stroke-linejoin="round" aria-hidden="true"><path d="M5 3h4l2 5-3 2a11 11 0 0 0 6 6l2-3 5 2v4a2 2 0 0 1-2 2A17 17 0 0 1 3 5a2 2 0 0 1 2-2z"/></svg>
      (555) 010 0187
    </li>
    <li>
      <svg viewBox="0 0 24 24" aria-hidden="true"><rect x="2" y="5" width="20" height="14" rx="1.5" fill="#e6e6e8"/><path d="M2.5 6l9.5 7 9.5-7" fill="none" stroke="#000" stroke-width="1.8"/></svg>
      nbramwit@velmordesign.example
    </li>
    <li>
      <svg viewBox="0 0 24 24" fill="none" stroke="#e6e6e8" stroke-width="2" aria-hidden="true"><circle cx="12" cy="12" r="9.5"/><path d="M2.5 12h19M12 2.5c3 3 3 16 0 19M12 2.5c-3 3-3 16 0 19"/></svg>
      velmordesign.example
    </li>
  </ul>

  <address class="address">
    2715 N Parkline Road<br>
    Ste 348, Marenby, ZZ 00148
  </address>
</section>

<section class="card card--back" aria-label="Business card back">
  <div class="back-mark" aria-hidden="true"></div>
  <div class="back-divider" aria-hidden="true"></div>
  <p class="wordmark"><span>Velmor</span><span>Home</span><span>Design</span></p>
</section>

</body>
</html>
```